School Poster and Prompt Design

I would like posters created for each of our school values (from the attached Way of Working document). In these posters I would like our logo, and some graphics or pictures - you can use the strategic plan attached for some examples.

I would also like a Code of Conduct Prompt for teachers and students (smaller design that can be used as a sticker for a laptop) based on the attached Tolworth Vale Essentials document. I have also attached a photo example, which we quite like that can be used for a base. This document is called example classroom management prompts.

Target Market(s)

School and students

Requirements
Must have
• Logo built into the design
Our school motto at the bottom 'Strive to Accomplish'
Design that incorporates elements that relate to each of the values.
Design that looks and feels like the example. In our school colours.
Nice to have
• Posters - Easy to read and understand from a distance.
Prompt - Easy to read and understand if turned into a sticker for a laptop.

```html
<!DOCTYPE html>
<html lang="en">
<head>
<meta charset="utf-8">
<title>Tolworth Vale | Way of Working – Classroom Routines</title>
<link href="https://fonts.googleapis.com/css2?family=Montserrat:wght@400;500;600;700;800&family=Work+Sans:wght@500;600;700&display=swap" rel="stylesheet">
<style>
  :root {
    --navy: #161a4d;
    --ink: #1b1d35;
    --sky: #2bb8ee;
    --sky-light: #7ed8f8;
    --sky-deep: #1785b1;
    --accent: #2a3f9c;
    --rule: #b9c2d4;
    --tick: #3aa7e6;
    --white: #ffffff;
  }
  * { box-sizing: border-box; margin: 0; padding: 0; }
  html, body { width: 800px; height: 1200px; overflow: hidden; background: var(--white); }
  body { font-family: "Work Sans", Arial, sans-serif; color: var(--ink); }
  .poster { position: relative; width: 800px; height: 1200px; background: var(--white); }
  .abs { position: absolute; }

  /* Header */
  .header { left: 0; top: 0; width: 800px; height: 193px; background: var(--navy); }
  .school-mark { left: 40px; top: 50px; width: 130px; text-align: center; color: var(--white);
    font-family: "Montserrat", sans-serif; font-weight: 700; font-size: 15px; line-height: 1.2; letter-spacing: 1px; }
  .school-mark .dot { width: 34px; height: 34px; border-radius: 50%; background: var(--sky); margin: 0 auto 10px; }
  .header-kicker { left: 192px; top: 60px; font-family: "Montserrat", sans-serif; font-weight: 400;
    font-size: 29px; color: var(--white); letter-spacing: 0.5px; white-space: nowrap; }
  .header-kicker .bar { display: inline-block; width: 2px; height: 28px; background: var(--white); margin: 0 12px; vertical-align: -4px; }
  .header-title { left: 190px; top: 105px; font-family: "Montserrat", sans-serif; font-weight: 800;
    font-size: 46px; color: var(--sky); letter-spacing: 1px; white-space: nowrap; }

  /* Section titles */
  .section-title { left: 0; width: 800px; text-align: center; font-family: "Montserrat", sans-serif;
    font-weight: 800; font-size: 44px; color: var(--ink); letter-spacing: 1px; }
  .title-rule { width: 184px; height: 1px; background: var(--rule); }
  .title-rule::after { content: ""; position: absolute; left: 68px; top: -2px; width: 48px; height: 5px; border-radius: 3px; background: var(--accent); }

  /* Entry */
  .entry-panel { left: 42px; top: 214px; width: 714px; height: 300px;
    background: linear-gradient(180deg, var(--sky-light) 0%, #3fb1dc 55%, var(--sky-deep) 100%);
    border: 3px solid #e8f7fd; box-shadow: 0 2px 6px rgba(0,0,0,.15); }
  .value-card { top: 336px; width: 184px; height: 152px; background: var(--white); border: 2px solid #d7eef8; text-align: center; }
  .value-card h3 { margin-top: 24px; font-family: "Montserrat", sans-serif; font-weight: 700; font-size: 19px; color: var(--navy); letter-spacing: 0.5px; }
  .value-card ul { list-style: none; margin-top: 8px; }
  .value-card li { font-size: 11px; font-weight: 600; line-height: 27px; color: var(--ink); }
  .value-icon { top: 314px; width: 42px; height: 42px; border-radius: 50%; background: #2fa9e0; border: 3px solid var(--white); }
  .tick { display: inline-block; width: 11px; height: 11px; vertical-align: -1px; margin-right: 5px; }
  .tick-lg { display: inline-block; width: 24px; height: 24px; }

  /* Start of lesson */
  .frame-sq { width: 11px; height: 11px; background: var(--navy); }
  .frame-h { left: 66px; width: 668px; height: 5px; border-top: 1px solid var(--accent); border-bottom: 1px solid var(--accent); }
  .frame-v { top: 562px; width: 5px; height: 153px; border-left: 1px solid var(--accent); border-right: 1px solid var(--accent); }
  .attend-box { left: 67px; top: 574px; width: 169px; height: 145px; background: var(--navy); color: var(--white);
    display: flex; align-items: center; justify-content: center; text-align: center; font-weight: 600; font-size: 15px; line-height: 1.18; padding: 0 14px; }
  .lesson-title { left: 262px; top: 586px; font-family: "Montserrat", sans-serif; font-weight: 800; font-size: 42px; color: var(--ink); letter-spacing: 1px; white-space: nowrap; }
  .lesson-sub { left: 263px; top: 638px; font-weight: 600; font-size: 20px; color: var(--ink); }
  .lesson-rule { left: 262px; top: 666px; width: 235px; height: 1px; background: var(--rule); }
  .lesson-rule::after { content: ""; position: absolute; left: 34px; top: -2px; width: 50px; height: 5px; border-radius: 3px; background: var(--accent); }
  .lesson-list { left: 262px; top: 692px; font-weight: 600; font-size: 15px; white-space: nowrap; }
  .lesson-list span { margin-right: 8px; }
  .lesson-list .tick { margin-right: 4px; }

  /* Exit */
  .exit-banner { left: 98px; top: 847px; width: 602px; height: 63px;
    background: linear-gradient(180deg, #6fd0f4 0%, #2aa0d2 100%); border: 2px solid #e6f6fc; box-shadow: 0 2px 5px rgba(0,0,0,.15);
    color: var(--white); text-align: center; font-weight: 700; font-size: 19px; line-height: 23px; padding-top: 7px; letter-spacing: 0.3px; }
  .exit-item { top: 964px; display: flex; gap: 10px; font-weight: 600; font-size: 21px; line-height: 23px; color: var(--ink); }
  .exit-divider { top: 941px; width: 1px; height: 75px; background: var(--rule); }

  /* Recognise */
  .recognise-band { left: 0; top: 1033px; width: 800px; height: 54px; background: var(--navy);
    color: var(--white); text-align: center; font-weight: 700; font-size: 23px; line-height: 54px; letter-spacing: 0.5px; }
  .reward { top: 1115px; display: flex; gap: 7px; font-weight: 600; font-size: 16px; line-height: 19px; color: var(--ink); }
  .reward .tick { margin-top: 3px; width: 13px; height: 13px; }
</style>
</head>
<body>
<svg width="0" height="0" style="position:absolute">
  <symbol id="tick" viewBox="0 0 24 24">
    <circle cx="12" cy="12" r="10" fill="none" stroke="currentColor" stroke-width="2"/>
    <path d="M7 12.5l3.4 3.4L21 5" fill="none" stroke="currentColor" stroke-width="2.4" stroke-linecap="round" stroke-linejoin="round"/>
  </symbol>
</svg>

<main class="poster">
  <header class="abs header">
    <div class="abs school-mark"><div class="dot"></div>TOLWORTH<br>VALE</div>
    <div class="abs header-kicker">TOLWORTH VALE<span class="bar"></span>WAY OF WORKING</div>
    <h1 class="abs header-title">CLASSROOM ROUTINES</h1>
  </header>

  <!-- Entry -->
  <section class="abs entry-panel"></section>
  <h2 class="abs section-title" style="top:236px">ENTRY</h2>
  <div class="abs title-rule" style="left:308px;top:294px"></div>

  <div class="abs value-card" style="left:80px">
    <h3>COMMITMENT</h3>
    <ul>
      <li><svg class="tick" style="color:var(--tick)"><use href="#tick"/></svg>On time</li>
      <li><svg class="tick" style="color:var(--tick)"><use href="#tick"/></svg>Correct uniform</li>
      <li><svg class="tick" style="color:var(--tick)"><use href="#tick"/></svg>Ready to learning</li>
    </ul>
  </div>
  <div class="abs value-card" style="left:308px">
    <h3>COURTESY</h3>
    <ul>
      <li><svg class="tick" style="color:var(--tick)"><use href="#tick"/></svg>In line</li>
      <li><svg class="tick" style="color:var(--tick)"><use href="#tick"/></svg>Waiting quietly</li>
      <li><svg class="tick" style="color:var(--tick)"><use href="#tick"/></svg>Stand behind chairs</li>
    </ul>
  </div>
  <div class="abs value-card" style="left:536px">
    <h3>COOPERATION</h3>
    <ul>
      <li><svg class="tick" style="color:var(--tick)"><use href="#tick"/></svg>In the right seat</li>
      <li><svg class="tick" style="color:var(--tick)"><use href="#tick"/></svg>Ready to participate</li>
      <li><svg class="tick" style="color:var(--tick)"><use href="#tick"/></svg>Actively listening</li>
    </ul>
  </div>

  <svg class="abs value-icon" style="left:151px" viewBox="0 0 42 42" aria-hidden="true">
    <g fill="none" stroke="#fff" stroke-width="2"><circle cx="16" cy="15" r="4"/><circle cx="26" cy="15" r="4"/><circle cx="16" cy="26" r="4"/><circle cx="26" cy="26" r="4"/></g>
  </svg>
  <svg class="abs value-icon" style="left:379px" viewBox="0 0 42 42" aria-hidden="true">
    <path d="M11 15l10-5 10 5-10 5z" fill="#fff"/><path d="M15 18v5c3 2 9 2 12 0v-5" fill="none" stroke="#fff" stroke-width="2"/>
    <path d="M10 29h22" stroke="#fff" stroke-width="3" stroke-linecap="round"/>
  </svg>
  <svg class="abs value-icon" style="left:607px" viewBox="0 0 42 42" aria-hidden="true">
    <path d="M14 22v-8M18 21v-10M22 21v-10M26 22v-8M13 22c0 6 4 9 8 9s8-3 8-9l2-4" fill="none" stroke="#fff" stroke-width="2.4" stroke-linecap="round"/>
  </svg>

  <!-- Start of lesson -->
  <div class="abs frame-sq" style="left:46px;top:537px"></div>
  <div class="abs frame-sq" style="left:743px;top:537px"></div>
  <div class="abs frame-sq" style="left:46px;top:739px"></div>
  <div class="abs frame-sq" style="left:743px;top:739px"></div>
  <div class="abs frame-h" style="top:540px"></div>
  <div class="abs frame-h" style="top:742px"></div>
  <div class="abs frame-v" style="left:47px"></div>
  <div class="abs frame-v" style="left:746px"></div>

  <div class="abs attend-box">Mark RollMark in the first 15 minutes and confirm with head count</div>
  <h2 class="abs lesson-title">START OF LESSON</h2>
  <p class="abs lesson-sub">Show and explain to students</p>
  <div class="abs lesson-rule"></div>
  <p class="abs lesson-list">
    <span><svg class="tick" style="color:var(--tick)"><use href="#tick"/></svg>Lesson Intention</span>
    <span><svg class="tick" style="color:var(--tick)"><use href="#tick"/></svg>Success Criteria</span>
    <span><svg class="tick" style="color:var(--tick)"><use href="#tick"/></svg>Way of Working Focus</span>
  </p>

  <!-- Exit -->
  <h2 class="abs section-title" style="top:764px">EXIT</h2>
  <div class="abs title-rule" style="left:308px;top:822px"></div>
  <div class="abs exit-banner">Exit strategy used to check for understanding<br>Before you leave...</div>

  <div class="abs exit-item" style="left:80px"><svg class="tick-lg" style="color:var(--navy)"><use href="#tick"/></svg><span>IT is<br>checked</span></div>
  <div class="abs exit-divider" style="left:239px"></div>
  <div class="abs exit-item" style="left:282px"><svg class="tick-lg" style="color:var(--navy)"><use href="#tick"/></svg><span>Environment left<br>neat and tidy</span></div>
  <div class="abs exit-divider" style="left:517px"></div>
  <div class="abs exit-item" style="left:551px"><svg class="tick-lg" style="color:var(--navy)"><use href="#tick"/></svg><span>Doors and<br>windows locked</span></div>

  <!-- Recognise -->
  <div class="abs recognise-band">RECOGNISE POSITIVE BEHAVIOUR BY</div>
  <div class="abs reward" style="left:62px"><svg class="tick" style="color:var(--tick)"><use href="#tick"/></svg><span>Assigning house points</span></div>
  <div class="abs reward" style="left:318px"><svg class="tick" style="color:var(--tick)"><use href="#tick"/></svg><span>Postcard or<br>Student of the Week</span></div>
  <div class="abs reward" style="left:556px"><svg class="tick" style="color:var(--tick)"><use href="#tick"/></svg><span>Phone call home</span></div>
</main>
</body>
</html>
```